Agribusiness Insurance

I would like postcard designed to attract farmers and agribusiness owners to my insurance consulting services. My business model is being a Trusted Advisor through identifying exposures, developing strategies, implementing programs and then monitoring our designed plan. I am knowledge representative (13YRs ag insurance), Represent 15 Farm + Carriers (favorable pricing/competitive multiple options) Specialized in Confinements, Cattle Farms, and Grain Producers. No Membership Fees Necessary

Many Insurance Producers in my area are nearing retirement I am 33 and am looking to promote this..

Target Market(s)

Farmers and Agribusiness Owners

Industry/Entity Type

Agribusiness

Requirements
Must have

• Owen Telfer
Phone: Cell 555 207 6413
Email: otelfer@ridgeplainagency.example

```html
<!DOCTYPE html>
<html lang="en">
<head>
<meta charset="utf-8">
<title>Agricultural Insurance Postcard</title>
<link rel="stylesheet" href="https://fonts.googleapis.com/css2?family=Roboto:wght@300;400&family=Roboto+Condensed:wght@700&family=Fira+Sans:wght@700&family=Open+Sans:wght@400;600&display=swap">
<style>
  :root {
    --royal: #0b2fe3;
    --white: #ffffff;
    --yellow: #ffea00;
    --ink: #111111;
    --sky: #4d8fd6;
    --cloud: #c9dcef;
    --grass-light: #b9d94a;
    --grass: #5f9a1f;
    --grass-dark: #2f5e12;
  }
  html, body {
    margin: 0;
    padding: 0;
    overflow: hidden;
  }
  .postcard {
    position: relative;
    width: 1200px;
    height: 926px;
    background: var(--royal);
    overflow: hidden;
    font-family: "Roboto", sans-serif;
    color: var(--white);
  }
  .field-scene {
    position: absolute;
    left: 0;
    top: 0;
    width: 676px;
    height: 926px;
    background: linear-gradient(180deg, var(--sky) 0%, var(--cloud) 28%, var(--sky) 42%, var(--grass-light) 55%, var(--grass) 75%, var(--grass-dark) 100%);
  }
  .headshot {
    position: absolute;
    left: 78px;
    top: 68px;
    width: 210px;
    height: 208px;
    border: 1px solid var(--white);
    padding: 6px;
    box-sizing: border-box;
  }
  .headshot-fill {
    width: 100%;
    height: 100%;
    background: radial-gradient(circle at 50% 40%, #9b8a80 0%, #6b5a52 55%, #3a2e2a 100%);
  }
  .agent {
    position: absolute;
    left: 82px;
    top: 282px;
    margin: 0;
    font-family: "Open Sans", sans-serif;
    color: var(--ink);
  }
  .agent-name {
    margin: 0;
    font-size: 33px;
    font-weight: 400;
    line-height: 44px;
    letter-spacing: -0.5px;
  }
  .agent-contact {
    margin: 6px 0 0;
    font-size: 22px;
    font-weight: 600;
    line-height: 32px;
  }
  .headline {
    position: absolute;
    left: 722px;
    top: 60px;
    margin: 0;
    font-family: "Fira Sans", sans-serif;
    font-weight: 700;
    font-size: 49px;
    line-height: 52px;
    letter-spacing: 3px;
  }
  .prompt {
    position: absolute;
    left: 720px;
    top: 232px;
    margin: 0;
    font-family: "Roboto Condensed", sans-serif;
    font-weight: 700;
    font-size: 43px;
    line-height: 56px;
    color: var(--yellow);
  }
  .needs {
    position: absolute;
    left: 720px;
    top: 302px;
    margin: 0;
    padding: 0;
    list-style: none;
    font-size: 35px;
    font-weight: 300;
    line-height: 40px;
  }
  .needs li { margin-bottom: 23px; }
  .needs li::before { content: "• "; }
  .needs .wrap { padding-left: 20px; text-indent: -20px; }
  .specialty-panel {
    position: absolute;
    left: 522px;
    top: 636px;
    width: 678px;
    height: 290px;
  }
  .specialty-text {
    position: absolute;
    left: 567px;
    top: 670px;
    margin: 0;
    font-size: 32px;
    font-weight: 300;
    line-height: 39px;
  }
  .fees {
    position: absolute;
    left: 567px;
    top: 802px;
    margin: 0;
    font-size: 32px;
    font-weight: 300;
    line-height: 40px;
  }
  .fees strong {
    font-family: "Roboto Condensed", sans-serif;
    font-weight: 700;
    color: var(--yellow);
  }
</style>
</head>
<body>
<div class="postcard">
  <div class="field-scene" role="img" aria-label="Painterly photo of tall green grass against a blue sky with clouds"></div>

  <div class="headshot">
    <div class="headshot-fill" role="img" aria-label="Portrait photo of agent Owen Telfer"></div>
  </div>
  <div class="agent">
    <p class="agent-name">Owen Telfer</p>
    <p class="agent-contact">Cell 555 207 6413<br>otelfer@ridgeplainagency.example</p>
  </div>

  <h1 class="headline">EXPERTS IN<br>AGRICULTURAL<br>INSURANCE</h1>
  <p class="prompt">Are you looking for:</p>
  <ul class="needs">
    <li>A new farm carrier?</li>
    <li class="wrap">A knowledgeable<br>representative?</li>
    <li>Lower Premium?</li>
    <li>More Options?</li>
    <li>Better Service</li>
  </ul>

  <svg class="specialty-panel" viewBox="0 0 678 290" aria-hidden="true">
    <polygon points="40,0 678,0 678,290 0,290 0,40" fill="var(--royal)"/>
  </svg>
  <p class="specialty-text">Specialized in<br>Confinements, Cattle Farms and<br>Grain Producers.</p>
  <p class="fees">No <strong>Membership Fees</strong> Necessary</p>
</div>
</body>
</html>
```